Tovrel Business Card

We are a modern retail clothing store. Established in 1994. I need a presentable card that will amaze vendors when given to them.

Front: Logo in middle
Info Side:

Name: Omar Latif
Cell: 630-555-0148
Work: 630-555-0192 EXT. 230
Email: Omar@tovrel.example
Website: www.Tovrel.example

Industry/Entity Type

Business

```html
<!DOCTYPE html>
<html lang="en">
<head>
<meta charset="utf-8">
<title>Tovrel Business Card</title>
<link href="https://fonts.googleapis.com/css2?family=Cabin:wght@400;600;700&display=swap" rel="stylesheet">
<style>
  :root {
    --backdrop: #d9d6d1;
    --card-black: #000000;
    --card-yellow: #f9df00;
    --ink: #111111;
    --accent: #f5d800;
  }
  * { box-sizing: border-box; margin: 0; padding: 0; }
  html, body {
    width: 1200px; height: 1000px; overflow: hidden;
    background: var(--backdrop);
    font-family: "Cabin", sans-serif;
  }
  .stage { position: relative; width: 1200px; height: 1000px; }
  .card {
    position: absolute; top: 128px; width: 437px; height: 744px;
    border-radius: 18px;
  }
  .card--front { left: 148px; background: var(--card-black); }
  .card--info { left: 615px; background: var(--card-yellow); }

  .wordmark {
    position: absolute; left: 0; right: 0; text-align: center;
    font-weight: 700; letter-spacing: 2px; line-height: 1;
  }
  .tagline {
    position: absolute; left: 0; right: 0; text-align: center;
    font-weight: 400; letter-spacing: 1px;
  }
  .card--front .wordmark { top: 490px; font-size: 86px; color: var(--accent); }
  .card--front .tagline { top: 582px; font-size: 24px; color: var(--accent); }
  .website {
    position: absolute; left: 0; right: 0; top: 682px; text-align: center;
    font-size: 22px; color: var(--accent);
  }

  .card--info .wordmark { top: 74px; font-size: 62px; color: var(--ink); }
  .card--info .tagline { top: 138px; font-size: 18px; color: var(--ink); }
  .holder-name {
    position: absolute; left: 0; right: 0; top: 357px; text-align: center;
    font-size: 24px; font-weight: 700; font-variant: small-caps; letter-spacing: 1px;
    color: var(--ink);
  }
  .contact-list {
    position: absolute; left: 0; right: 0; top: 496px; list-style: none;
    text-align: center; color: var(--ink); font-size: 21px;
  }
  .contact-item { display: flex; flex-direction: column; align-items: center; }
  .contact-item + .contact-item { margin-top: 10px; }
  .contact-icon { width: 28px; height: 28px; margin-bottom: 4px; }
</style>
</head>
<body>
<main class="stage">
  <section class="card card--front">
    <div class="wordmark">Tovrel</div>
    <div class="tagline">Fashion Retailer</div>
    <div class="website">www.Tovrel.example</div>
  </section>

  <section class="card card--info">
    <div class="wordmark">Tovrel</div>
    <div class="tagline">Fashion Retailer</div>
    <div class="holder-name">Omar Latif</div>
    <ul class="contact-list">
      <li class="contact-item">
        <svg class="contact-icon" viewBox="0 0 28 28" aria-hidden="true">
          <rect x="9" y="3" width="11" height="22" rx="1.5" fill="none" stroke="#111" stroke-width="2"/>
          <rect x="11" y="6" width="7" height="6" fill="#111"/>
          <g fill="#111"><rect x="11" y="14" width="2" height="2"/><rect x="14" y="14" width="2" height="2"/><rect x="17" y="14" width="1.5" height="2"/><rect x="11" y="18" width="2" height="2"/><rect x="14" y="18" width="2" height="2"/><rect x="17" y="18" width="1.5" height="2"/></g>
          <line x1="10" y1="3" x2="10" y2="0.5" stroke="#111" stroke-width="1.6"/>
        </svg>
        <span>630-555-0148</span>
      </li>
      <li class="contact-item">
        <svg class="contact-icon" viewBox="0 0 28 28" aria-hidden="true">
          <circle cx="14" cy="14" r="12" fill="none" stroke="#111" stroke-width="1.8"/>
          <path d="M10 8 l3 -1 l2 4 l-2 1.5 q1 3 3.5 5 l1.5 -2 l4 2 l-1 3 q-6 1 -10 -5 q-3 -4 -1 -7.5z" fill="#111"/>
        </svg>
        <span>630-555-0192 EXT. 230</span>
      </li>
      <li class="contact-item">
        <svg class="contact-icon" viewBox="0 0 28 28" aria-hidden="true">
          <rect x="2" y="6" width="24" height="16" fill="none" stroke="#111" stroke-width="1.6"/>
          <path d="M2 6 L14 16 L26 6 M2 22 L11 13.5 M26 22 L17 13.5" fill="none" stroke="#111" stroke-width="1.4"/>
        </svg>
        <span>Omar@tovrel.example</span>
      </li>
    </ul>
  </section>
</main>
</body>
</html>
```